harbor lantern security & electric needs a business card

Must be attractive and modern, look professional and upscale!!
We provide alarm and cameras services and 24 hour monitoring for commercial and residential clients. In addition, the owner is a master electrician that provides services to commercial and residential clients.
We also install and service automatic gates. We previously had two different businesses but decided to merge into one, thus creating Harbor Lantern Security & Electric.

Target Market(s)

Commercial Business and residential customers

Industry/Entity Type

Security

Contact Information for Business Card

Front and back design with logo and services listed

Font styles to use
Sans Serif

Colors
ec1f27
0355a3
fbee3f

Requirements
Must have
• Front of card:
• Marcus Tremblow-Owner
• telephone icon and then the number 936-555-0193
• Mail icon and then email address mtremblow@quillmail.example
• World Icon then website www.yourharborlanterntx.example
• Location marker and then Alderbrook, Rivermark
• We would like to have a picture of the logo at least on the front
• Also need motto on front: We're There When You're Not
• The front of the card must also say Licensed and Insured in addition to:
• License Number: K47315
• TECL: 58629
• On the Back of the Card:
• List each of these Services with check marks:
• Residential and Commercial Electrical Services
• Electric Gates
• Alarm Systems
• Alarm Monitoring
• Cameras
• ***Use separate attached logo, the business card design is just to be used as a model***
Nice to have
• It would be nice to have the logo on back of the card in addition to these words at the bottom:
• "No job too big or small, we do it all!"
Should not have
• Anything crazy!!

```html
<!DOCTYPE html>
<html lang="en">
<head>
<meta charset="utf-8">
<title>Harbor Lantern Security &amp; Electric — Business Card</title>
<link rel="stylesheet" href="https://fonts.googleapis.com/css2?family=Lato:wght@400;700;900&display=swap">
<style>
  :root {
    --navy: #2b4677;
    --red: #ec2227;
    --white: #ffffff;
    --stage: #222222;
  }
  * { box-sizing: border-box; margin: 0; padding: 0; }
  html, body { width: 1189px; height: 1200px; overflow: hidden; background: var(--stage); }
  body { position: relative; font-family: "Lato", sans-serif; color: var(--navy); }

  .card {
    position: absolute; left: 171px; width: 855px; height: 486px;
    background: var(--white); border-radius: 24px; overflow: hidden;
    box-shadow: 0 6px 14px rgba(0,0,0,.55);
  }
  .card--front { top: 67px; }
  .card--back { top: 625px; height: 487px; }

  /* front */
  .front__band { position: absolute; left: 0; top: 0; width: 100%; height: 164px; background: var(--navy); }
  .front__stripe { position: absolute; left: 0; top: 164px; width: 100%; height: 8px; background: var(--red); }
  .brand-mark { position: absolute; background: var(--red); }
  .front .brand-mark { left: 178px; top: 50px; width: 100px; height: 100px; }
  .brand-name { position: absolute; font-weight: 900; color: var(--navy); text-align: center; line-height: 1.05; }
  .front .brand-name { left: 30px; top: 196px; width: 396px; font-size: 40px; }
  .brand-name__sub { display: block; font-size: 20px; letter-spacing: 1px; margin-top: 4px; }

  .owner { position: absolute; right: 43px; top: 52px; text-align: right; }
  .owner__name { font-size: 32px; font-weight: 700; color: var(--white); line-height: 1; }
  .owner__role { font-size: 23px; color: var(--red); line-height: 1.05; }

  .motto { position: absolute; right: 43px; top: 248px; font-size: 23px; color: var(--navy); }

  .contact { position: absolute; left: 45px; top: 318px; list-style: none; }
  .contact__item { display: flex; align-items: center; height: 31.5px; font-size: 23px; }
  .contact__icon { width: 22px; height: 20px; margin-right: 11px; fill: var(--red); flex: none; }
  .contact__icon--outline { fill: none; stroke: var(--red); stroke-width: 1.8; }

  .license { position: absolute; right: 43px; top: 385px; font-size: 23px; line-height: 28px; }

  .front__foot-red { position: absolute; left: 0; bottom: 0; width: 429px; height: 21px; background: var(--red); }
  .front__foot-navy { position: absolute; left: 429px; bottom: 0; right: 0; height: 21px; background: var(--navy); }

  /* back */
  .back .brand-mark { left: 155px; top: 100px; width: 100px; height: 100px; }
  .back .brand-name { left: 40px; top: 222px; width: 330px; font-size: 36px; }

  .services { position: absolute; left: 460px; top: 104px; }
  .services__title { font-size: 31px; font-weight: 700; color: var(--red); line-height: 1; margin-bottom: 30px; }
  .services__list { list-style: none; }
  .services__item { display: flex; align-items: center; height: 28.5px; font-size: 24px; }
  .services__tick { width: 22px; height: 20px; margin-right: 11px; fill: var(--red); flex: none; }

  .back__stripe { position: absolute; left: 0; top: 433px; width: 427px; height: 5px; background: var(--red); }
  .back__foot { position: absolute; left: 0; top: 433px; right: 0; bottom: 0; background: var(--navy);
    clip-path: polygon(427px 0, 100% 0, 100% 100%, 0 100%, 0 5px, 427px 5px); }
  .slogan { position: absolute; left: 0; right: 0; top: 449px; text-align: center; font-size: 21px; letter-spacing: 2.5px; color: var(--white); }
</style>
</head>
<body>

<section class="card card--front front" aria-label="Business card front">
  <div class="front__band"></div>
  <div class="front__stripe"></div>
  <div class="brand-mark"></div>
  <div class="brand-name">Harbor Lantern<span class="brand-name__sub">Security &amp; Electric</span></div>

  <div class="owner">
    <div class="owner__name">MARCUS TREMBLOW</div>
    <div class="owner__role">Owner</div>
  </div>

  <p class="motto">We're There When You're Not</p>

  <ul class="contact">
    <li class="contact__item">
      <svg class="contact__icon" viewBox="0 0 24 24"><path d="M12 2a7 7 0 0 0-7 7c0 5 7 13 7 13s7-8 7-13a7 7 0 0 0-7-7zm0 3a4 4 0 1 1 0 8 4 4 0 0 1 0-8z"/></svg>
      Alderbrook, Rivermark</li>
    <li class="contact__item">
      <svg class="contact__icon" viewBox="0 0 24 24"><path d="M2 8c2-3 6-4 10-4s8 1 10 4l-1 3-4-1V8H7v2l-4 1zM6 12h12l2 8H4z"/></svg>
      936-555-0193</li>
    <li class="contact__item">
      <svg class="contact__icon" viewBox="0 0 24 24"><path d="M2 5h20v14H2zm2 2v1l8 6 8-6V7l-8 6z"/></svg>
      mtremblow@quillmail.example</li>
    <li class="contact__item">
      <svg class="contact__icon contact__icon--outline" viewBox="0 0 24 24"><circle cx="12" cy="12" r="9"/><ellipse cx="12" cy="12" rx="4" ry="9"/><path d="M3 12h18M5 7h14M5 17h14"/></svg>
      www.yourharborlanterntx.example</li>
  </ul>

  <div class="license">License Number: K47315<br>TECL: 58629</div>

  <div class="front__foot-red"></div>
  <div class="front__foot-navy"></div>
</section>

<section class="card card--back back" aria-label="Business card back">
  <div class="brand-mark"></div>
  <div class="brand-name">Harbor Lantern<span class="brand-name__sub">Security &amp; Electric</span></div>

  <div class="services">
    <h2 class="services__title">SERVICES</h2>
    <ul class="services__list">
      <li class="services__item"><svg class="services__tick" viewBox="0 0 24 24"><path d="M2 13l4-3 4 4 10-11 3 3-13 15z"/></svg>Residential and Commercial</li>
      <li class="services__item"><svg class="services__tick" viewBox="0 0 24 24"><path d="M2 13l4-3 4 4 10-11 3 3-13 15z"/></svg>Electrical Services</li>
      <li class="services__item"><svg class="services__tick" viewBox="0 0 24 24"><path d="M2 13l4-3 4 4 10-11 3 3-13 15z"/></svg>Electric Gates</li>
      <li class="services__item"><svg class="services__tick" viewBox="0 0 24 24"><path d="M2 13l4-3 4 4 10-11 3 3-13 15z"/></svg>Alarm Systems</li>
      <li class="services__item"><svg class="services__tick" viewBox="0 0 24 24"><path d="M2 13l4-3 4 4 10-11 3 3-13 15z"/></svg>Alarm Monitoring</li>
      <li class="services__item"><svg class="services__tick" viewBox="0 0 24 24"><path d="M2 13l4-3 4 4 10-11 3 3-13 15z"/></svg>Cameras</li>
    </ul>
  </div>

  <div class="back__stripe"></div>
  <div class="back__foot"></div>
  <p class="slogan">No job too big or small, we do it all!</p>
</section>

</body>
</html>
```